Drywall plastering business card design

Attached is my new logo and a picture of my current business card. I would like my new logo incorporated in to the business card and also my website which is:
www.ridgecrestwallfinishers.co.nz
Industry/Entity Type
Business
Contact Information for Business Card
I would like a picture of my van and my new logo on my new business card. See attached files for pictures of my old business card, van picture and logo.
Colors
0555a3
ffffff
Requirements
Must have
- New logo, Van, contact info

```html
<!DOCTYPE html>
<html lang="en">
<head>
<meta charset="utf-8">
<title>Ridgecrest Wall Finishers – Business Card</title>
<link href="https://fonts.googleapis.com/css2?family=Lato:wght@400;700;900&family=Yellowtail&display=swap" rel="stylesheet">
<style>
  :root {
    --page-bg: #e9e7e4;
    --card-dark: #1a1c1f;
    --card-mid: #2a2d31;
    --brand-blue: #0a6fc2;
    --brand-deep: #0555a3;
    --white: #ffffff;
    --logo-panel: #f2f2f2;
    --van-light: #d9dde2;
    --van-dark: #8f98a3;
  }
  * { box-sizing: border-box; margin: 0; padding: 0; }
  html, body {
    width: 1200px;
    height: 900px;
    overflow: hidden;
    background: var(--page-bg);
  }
  .canvas {
    position: relative;
    width: 1200px;
    height: 900px;
    display: flex;
    align-items: center;
    justify-content: center;
  }
  .business-card {
    position: relative;
    width: 1000px;
    height: 572px;
    background: radial-gradient(ellipse at 70% 30%, var(--card-mid) 0%, var(--card-dark) 75%);
    box-shadow: 0 18px 40px rgba(0,0,0,0.25);
    overflow: hidden;
  }
  .logo-panel {
    position: absolute;
    left: 48px;
    top: 0;
    width: 300px;
    height: 340px;
    background: var(--logo-panel);
    display: flex;
    align-items: center;
    justify-content: center;
    gap: 14px;
    padding: 0 22px;
  }
  .logo-mark {
    flex: none;
    width: 26px;
    height: 26px;
    background: var(--brand-deep);
  }
  .logo-name {
    font-family: 'Lato', sans-serif;
    font-weight: 900;
    font-size: 30px;
    line-height: 1.05;
    text-transform: uppercase;
    color: var(--brand-deep);
  }
  .van-photo {
    position: absolute;
    right: 40px;
    top: 30px;
    width: 250px;
    height: 80px;
    background: linear-gradient(180deg, var(--van-light) 0%, var(--van-dark) 100%);
  }
  .contact {
    position: absolute;
    left: 385px;
    top: 122px;
    font-family: 'Lato', sans-serif;
    color: var(--white);
  }
  .contact-name {
    font-weight: 700;
    font-size: 38px;
    letter-spacing: 0.5px;
    line-height: 1.1;
  }
  .contact-role {
    font-size: 25px;
    color: var(--brand-blue);
    margin-left: 10px;
    margin-top: 2px;
  }
  .contact-lines {
    margin-top: 20px;
    font-size: 23px;
    line-height: 1.4;
    list-style: none;
    white-space: nowrap;
  }
  .contact-lines .label {
    color: var(--brand-blue);
    margin-right: 6px;
  }
  .tagline {
    position: absolute;
    left: 0;
    right: 0;
    top: 412px;
    text-align: center;
    white-space: nowrap;
    font-family: 'Yellowtail', cursive;
    font-size: 48px;
    color: var(--brand-blue);
    letter-spacing: 1px;
  }
</style>
</head>
<body>
  <main class="canvas">
    <article class="business-card">
      <div class="logo-panel">
        <span class="logo-mark" aria-hidden="true"></span>
        <span class="logo-name">Ridgecrest Wall Finishers</span>
      </div>
      <div class="van-photo" role="img" aria-label="Photo of the company van"></div>
      <section class="contact">
        <h1 class="contact-name">MARK HALDEN</h1>
        <p class="contact-role">Proprietor</p>
        <ul class="contact-lines">
          <li><span class="label">P:</span>027 555 01 42</li>
          <li><span class="label">E:</span>ridgecrestwallfinishers@gmail.com</li>
          <li><span class="label">W:</span>www.ridgecrestwallfinishers.co.nz</li>
        </ul>
      </section>
      <p class="tagline">Large Jobs or Small - Always Quality Assured</p>
    </article>
  </main>
</body>
</html>
```